Fully coded Word press template and New logo for Colocation Provider

We need a wordpress template and new logo for our website. The current website is vornlukhost.net. Vornluk Host is a colocation provider located in San Antonio Texas. We are looking for a complete re-design of the site and logo. Everything is on the table. New colors, logo, look, feel...everything. Go wild! We are looking for a clean modern look.

P.S. The name Vornluk originated from the Glimmer Forge movies (Vornluk is where the work was done).

Target Market(s)

We are targeting toward IT staffs and CFO's

Requirements
Must have
• Must have clean look. Although can have some playfulness too it, It must convey safety and security.

```html
<!DOCTYPE html>
<html lang="en">
<head>
<meta charset="utf-8">
<title>Vornluk Host Services LLC</title>
<link rel="stylesheet" href="https://fonts.googleapis.com/css2?family=Cinzel:wght@600&family=Oswald:wght@400&family=Open+Sans:wght@400&display=swap">
<style>
:root{
  --shell:#2f2f30;
  --shell-dark:#242425;
  --nav-top:#4a4a4c;
  --nav-bottom:#2a2a2b;
  --brand:#16b4e6;
  --ink:#1c1c1c;
  --body-text:#444;
  --muted:#8a8a8a;
  --heading:#3c4a5e;
  --accent:#c0271e;
  --panel:#f3f3f3;
  --footer-text:#e2e2e2;
}
*{box-sizing:border-box;margin:0;padding:0}
html,body{width:1082px;height:1200px;overflow:hidden;background:#fff}
.page{position:relative;width:1050px;height:1164px;transform:scale(1.0305);transform-origin:0 0;font-family:"Open Sans",Arial,sans-serif}
.abs{position:absolute}

.header{left:50px;top:0;width:952px;height:124px;background:var(--shell)}
.brand{left:24px;top:18px;display:flex;align-items:center;gap:8px;color:var(--brand);font-family:"Open Sans",Arial,sans-serif;font-size:22px;font-weight:400;letter-spacing:-.3px}
.brand-mark{width:32px;height:32px;border-radius:50%;background:var(--brand)}
.search{left:698px;top:28px;width:240px;height:40px;border-radius:4px;background:var(--shell-dark);box-shadow:inset 0 1px 3px #000;color:#ddd;font-size:13px;font-family:Arial,sans-serif;padding:12px 13px}
.search-btn{position:absolute;right:4px;top:4px;width:32px;height:32px;border-radius:3px;background:linear-gradient(#8a8a8a,#5a5a5a)}
.nav{left:0;top:84px;width:952px;height:40px;display:flex;background:linear-gradient(var(--nav-top),var(--nav-bottom));border-top:1px solid #1a1a1a}
.nav a{display:block;height:40px;line-height:40px;color:#fff;font:bold 11px Arial,sans-serif;text-decoration:none;text-align:center;border-right:1px solid #1d1d1d;border-left:1px solid #555}
.nav a.active{background:linear-gradient(#2a2a2b,#3a3a3c)}

.slider{left:56px;top:137px;width:940px;height:350px;background:linear-gradient(100deg,#b9bcc6 0%,#2a2b2e 30%,#1b1b1d 55%,#a9acb6 80%,#cfd1d8 100%);box-shadow:0 12px 30px rgba(0,0,0,.35)}
.slide-arrow{top:144px;width:60px;height:60px;background:rgba(120,120,120,.6)}
.caption{left:0;top:256px;width:940px;height:94px;background:rgba(60,60,62,.82);color:#fff;padding:10px 30px}
.caption h2{font:400 22px Arial,sans-serif;color:#e8e8e8;margin-bottom:6px}
.caption p{font:12px/18px Arial,sans-serif;color:#f2f2f2}
.read-more{right:32px;top:15px;height:20px;width:80px;border-radius:10px;background:linear-gradient(#fff,#ccc);font:10px/20px Arial,sans-serif;color:#333;padding-left:8px}

.welcome{left:56px;top:517px;width:928px;height:96px;background:var(--panel);border-bottom:1px solid #ddd;padding:20px 18px}
.welcome h1{font:600 25px "Cinzel",serif;color:var(--heading);letter-spacing:1px}
.welcome p{font:16px Arial,sans-serif;color:var(--muted);margin-top:2px;padding-left:3px}
.pen{right:14px;top:2px;width:70px;height:76px}

.login-tab{left:1010px;top:552px;width:40px;height:170px;border-radius:6px 0 0 6px;background:linear-gradient(90deg,#e6e6e6,#cfcfcf);border:1px solid #bbb}
.login-tab span{position:absolute;left:12px;top:135px;transform:rotate(-90deg);transform-origin:0 0;font:bold 12px Arial,sans-serif;color:#555;white-space:nowrap}

.feature{top:640px;width:275px}
.feature h3{font:400 16px "Oswald",sans-serif;color:var(--heading);text-transform:uppercase;letter-spacing:-.2px;margin-bottom:6px}
.feature .photo{width:273px;height:153px;border:1px solid #ccc;padding:3px}
.feature .photo div{width:100%;height:100%}
.feature p{margin-top:12px;font:10.5px/18px "Open Sans",sans-serif;color:var(--body-text);height:108px}
.see-more{display:block;font-size:12px;color:var(--accent);text-decoration:underline;margin-top:2px}
.feature h4{position:absolute;top:334px;left:0;width:260px;font:400 12.5px/18px "Open Sans",sans-serif;color:var(--ink)}
.go{position:absolute;top:354px;left:234px;width:22px;height:22px}

.footer{left:50px;top:1038px;width:952px;height:126px;background:var(--shell);color:var(--footer-text);font:12.5px "Open Sans",sans-serif}
.footer .links{left:31px;top:24px}
.footer .copy{left:31px;top:48px}
.footer .connect{right:28px;top:24px}
.social{right:28px;top:54px;display:flex;gap:14px}
.social i{display:block;width:26px;height:26px;border-radius:3px}
</style>
</head>
<body>
<div class="page">
  <header class="header abs">
    <div class="brand abs"><span class="brand-mark"></span>Vornluk Host Services LLC</div>
    <div class="search abs">Search<span class="search-btn"><svg width="32" height="32" viewBox="0 0 32 32"><circle cx="14" cy="14" r="6" fill="none" stroke="#fff" stroke-width="2.5"/><line x1="18.5" y1="18.5" x2="24" y2="24" stroke="#fff" stroke-width="3"/></svg></span></div>
    <nav class="nav abs">
      <a style="width:125px">SERVICE</a>
      <a style="width:146px">SAVEFTY &amp; SECURITY</a>
      <a class="active" style="width:186px">DATA CENTER SPECIFICATION</a>
      <a style="width:120px">ABOUT US</a>
      <a style="width:122px">CONTACT US</a>
    </nav>
  </header>

  <section class="slider abs" role="img" aria-label="Data center aisle with rows of black server racks">
    <div class="slide-arrow abs" style="left:29px"><svg width="60" height="60"><polyline points="35,20 25,30 35,40" fill="none" stroke="#ddd" stroke-width="4"/></svg></div>
    <div class="slide-arrow abs" style="left:848px"><svg width="60" height="60"><polyline points="25,20 35,30 25,40" fill="none" stroke="#ddd" stroke-width="4"/></svg></div>
    <div class="caption abs">
      <h2>Why Vornluk</h2>
      <p>You need safe, always-on data, and you need unwavering confidence in the partner you choose to manage it. With a potent combination of upscale technological sophistication and down-home trustworthy service, Vornluk is the reliable, user-friendly data center solution your growing business demands.</p>
      <div class="read-more abs">Read More <svg width="10" height="10" style="position:absolute;right:6px;top:5px"><polygon points="2,1 8,5 2,9" fill="#333"/></svg></div>
    </div>
  </section>

  <section class="welcome abs">
    <h1>WELCOME TO OUR SITE</h1>
    <p>You need safe, always-on data, and you need unwavering confidence in the partner you choose to manage it.</p>
    <div class="pen abs" role="img" aria-label="Fountain pen drawing a signature line" style="background:linear-gradient(135deg,#f3f3f3,#c9a23a 50%,#555 70%,#f3f3f3)"></div>
  </section>

  <div class="login-tab abs"><span>CLIENT LOGIN</span></div>

  <article class="feature abs" style="left:74px">
    <h3>Safe, Secure, Invisible</h3>
    <div class="photo"><div role="img" aria-label="Steel chain locked with a brass padlock" style="background:linear-gradient(160deg,#fff,#b9b9b9 50%,#c8a857 75%,#fff)"></div></div>
    <p>Thieves can't steal it if they don't know it's there, which is why the Vornluk Data Center facility is built to be invisible. And even if they stumble across us, they have to get in – and back out – to pose a threat to your data. Vornluk's commitment to security best practices ensure that this threat is nullified.</p>
    <a class="see-more">See More</a>
    <h4>Tour The Most Secure Data Facility In Texas</h4>
    <svg class="go" viewBox="0 0 22 22"><circle cx="11" cy="11" r="10" fill="#666"/><polyline points="6,6 10,11 6,16" fill="none" stroke="#fff" stroke-width="2"/><polyline points="11,6 15,11 11,16" fill="none" stroke="#fff" stroke-width="2"/></svg>
  </article>

  <article class="feature abs" style="left:396px">
    <h3>Lower Total Cost of Ownership</h3>
    <div class="photo"><div role="img" aria-label="Crowd of grey figures around one red figure on a pedestal" style="background:linear-gradient(180deg,#fff,#6b6b6b 60%,#e4e4e4)"></div></div>
    <p>The appeal of outsourcing is that it strengthens your cash flow while freeing your company's decision makers from the minutiae of IT management. Vornluk's revolutionary design features help maximize the financial rewards of outsourcing, both now and over the long term.</p>
    <a class="see-more">See More</a>
    <h4>How Data Outsourcing Can Strengthen Your Bottom Line</h4>
    <svg class="go" viewBox="0 0 22 22"><circle cx="11" cy="11" r="10" fill="#666"/><polyline points="6,6 10,11 6,16" fill="none" stroke="#fff" stroke-width="2"/><polyline points="11,6 15,11 11,16" fill="none" stroke="#fff" stroke-width="2"/></svg>
  </article>

  <article class="feature abs" style="left:708px">
    <h3>Disaster Avoidance</h3>
    <div class="photo"><div role="img" aria-label="Red figures crossing a plank over a crack toward a help sign" style="background:linear-gradient(160deg,#fff,#3a3a3a 45%,#fff 60%,#c8302a)"></div></div>
    <p>If the biggest known threat to data security were sand, would you store your data on the beach? Neither would we. That's why we chose the mild climate and stable meteorological conditions of San Antonio to securely house your data in.</p>
    <a class="see-more">See More</a>
    <h4>See How Security Begins At (Our) Home</h4>
    <svg class="go" viewBox="0 0 22 22"><circle cx="11" cy="11" r="10" fill="#666"/><polyline points="6,6 10,11 6,16" fill="none" stroke="#fff" stroke-width="2"/><polyline points="11,6 15,11 11,16" fill="none" stroke="#fff" stroke-width="2"/></svg>
  </article>

  <footer class="footer abs">
    <div class="links abs">Home | Services | Safety &amp; Security | Data Center Specifications | About Us | Contact Us</div>
    <div class="copy abs">Copyright 2010 Vornluk Host Services, All Rights Reserved.</div>
    <div class="connect abs">Conncect With Us</div>
    <div class="social abs">
      <i style="background:#3b5998"></i><i style="background:#4ab3e0"></i><i style="background:#f07c1f"></i><i style="background:#1b86bd"></i><i style="background:#2a6fb0"></i>
    </div>
  </footer>
</div>
</body>
</html>
```